New design of old website

We need a new design of our domain name reseller website.

quilanorte.com

we would also like new design for Logo and all.

the site will be in English and portuguesse,

Industry/Entity Type

Domain

```html
<!DOCTYPE html>
<html lang="en">
<head>
<meta charset="utf-8">
<title>QuilaNorte – ccTLD Experts</title>
<link rel="stylesheet" href="https://fonts.googleapis.com/css2?family=Arimo:wght@400;700&display=swap">
<style>
:root{
  --orange:#f07a26;
  --orange-light:#f4a866;
  --orange-text:#e8631c;
  --dark:#3a3a3a;
  --dark-2:#555;
  --grey-text:#6f6f6f;
  --light-bg:#f4f4f4;
  --white:#fff;
  --line:#d9d9d9;
}
*{box-sizing:border-box;margin:0;padding:0}
html,body{width:1200px;height:1148px;overflow:hidden}
body{position:relative;background:var(--white);font-family:"Arimo",Arial,sans-serif;color:var(--grey-text)}
.abs{position:absolute}

/* top bar */
.topbar{left:0;top:0;width:1200px;height:60px;background:linear-gradient(#4a4a4a,#2f2f2f)}
.top-links{right:420px;top:20px;color:#eee;font-size:15px;letter-spacing:.3px}
.top-links span{margin:0 10px}
.search{left:847px;top:16px;width:169px;height:29px;background:#fff;border:1px solid #ccc;font-size:12px;color:#333;padding:7px 12px}
.search svg{position:absolute;right:8px;top:5px}
.lang{left:1026px;top:16px;width:86px;height:29px;background:#fff;border:1px solid #ccc;font-size:12px;color:#333;padding:6px 10px 0 32px}
.lang .flag{position:absolute;left:10px;top:9px;width:16px;height:11px;background:#2b3f8f;border:1px solid #ccc}
.lang svg{position:absolute;right:9px;top:11px}

/* header */
.header{left:0;top:60px;width:1200px;height:151px;background:linear-gradient(#fdfdfd,#eeeeee 60%,#fff)}
.brand{left:92px;top:112px;display:flex;align-items:center;gap:12px}
.brand-dot{width:34px;height:34px;border-radius:50%;background:var(--orange)}
.brand-name{font-size:44px;font-weight:700;color:var(--orange)}
.nav{left:561px;top:107px;height:55px;display:flex;border:1px solid #d4d4d4;border-radius:6px;background:linear-gradient(#fafafa,#e6e6e6);box-shadow:0 2px 4px rgba(0,0,0,.1)}
.nav a{display:block;padding:0 13px;line-height:53px;font-size:13.5px;color:#555;text-decoration:none;border-right:1px solid #d0d0d0}
.nav a:last-child{border-right:0}
.nav a.active{color:var(--orange-text)}

/* hero */
.hero{left:0;top:211px;width:1200px;height:358px;background:radial-gradient(ellipse at 40% 40%,#f6b57a 0%,#f29a50 45%,var(--orange) 85%)}
.map{left:104px;top:245px;width:527px;height:297px;background:linear-gradient(#fff,#fbe4d0);opacity:.9;border-radius:40px 80px 30px 60px}
.hero-title{left:683px;top:332px;font-size:38px;font-weight:700;color:#fff;letter-spacing:1px}
.hero-tag{left:681px;top:391px;width:326px;height:49px;background:#f8c79b;border-radius:6px;font-size:15.5px;font-weight:700;color:#3a2a1c;padding:15px 0 0 17px}
.dots{left:924px;top:464px;display:flex;gap:8px}
.dots i{width:14px;height:14px;border-radius:50%;background:#444}
.dots i.on{background:transparent;border:2px solid #fff}

/* features */
.features{left:88px;top:542px;width:1023px;height:222px;background:#fff}
.feature{top:552px;width:244px;height:210px;background:linear-gradient(#fff,#f1f1f1);box-shadow:0 3px 5px rgba(0,0,0,.08);text-align:center}
.feature .icon{width:90px;height:90px;margin:10px auto 0;border-radius:12px}
.feature h3{margin-top:30px;font-size:19px;font-weight:700;color:var(--orange-text);letter-spacing:.5px}
.feature p{margin-top:8px;font-size:13.5px;line-height:19px;color:var(--grey-text)}

/* welcome */
.welcome-title{left:96px;top:800px;font-size:21px;font-weight:700;color:var(--orange-text);letter-spacing:.5px}
.welcome-sub{left:96px;top:839px;font-size:16px;color:var(--orange-text)}
.welcome-text{left:96px;top:866px;width:758px;font-size:13.3px;line-height:23px;color:var(--grey-text)}
.btn{left:95px;top:951px;width:94px;height:36px;background:linear-gradient(#5a5a5a,#333);border:1px solid #222;border-radius:4px;color:#fff;font-size:12.5px;font-weight:700;text-align:center;line-height:34px}
.photo-frame{left:870px;top:804px;width:231px;height:182px;border:1px solid var(--line);background:#fff;padding:4px}
.photo{width:100%;height:100%;background:radial-gradient(circle at 45% 35%,#c8d6df,#6c8090 70%,#4a5b67)}

/* tabs */
.tab{top:1020px;width:197px;height:44px;background:linear-gradient(#777,#4b4b4b);border:1px solid #3a3a3a;color:#fff;font-weight:700;font-size:15.5px;text-align:center;line-height:42px;letter-spacing:.5px}
.tab.active{background:linear-gradient(#f7a35a,var(--orange));border-color:#e07020}

/* footer */
.footer{left:0;top:1078px;width:1200px;height:70px;background:#3d3d3d}
.foot-links{left:88px;top:1094px;font-size:12.5px;color:#cfcfcf}
.foot-links span{margin:0 7px;color:#999}
.copyright{left:88px;top:1120px;font-size:12.5px;color:#cfcfcf}
.social{left:980px;top:1100px;display:flex;gap:9px}
.social i{width:26px;height:26px;border-radius:50%;background:#777;position:relative}
</style>
</head>
<body>

<div class="abs topbar"></div>
<div class="abs top-links">REGISTER<span>|</span>LOGIN</div>
<div class="abs search">Search
  <svg width="18" height="18" viewBox="0 0 18 18"><circle cx="7" cy="7" r="5" fill="none" stroke="#222" stroke-width="2.5"/><line x1="11" y1="11" x2="16" y2="16" stroke="#222" stroke-width="3"/></svg>
</div>
<div class="abs lang"><span class="flag"></span>Eng
  <svg width="10" height="6" viewBox="0 0 10 6"><path d="M0 0h10L5 6z" fill="#444"/></svg>
</div>

<div class="abs header"></div>
<div class="abs brand"><span class="brand-dot"></span><span class="brand-name">QuilaNorte</span></div>
<nav class="abs nav">
  <a class="active" href="#">HOME</a><a href="#">WHY QUILA</a><a href="#">PRODUCTS</a><a href="#">SERVICES</a><a href="#">RESELLER</a><a href="#">CONTACT</a>
</nav>

<div class="abs hero"></div>
<div class="abs map" role="img" aria-label="White world map with location pins"></div>
<div class="abs hero-title">CCTLD EXPERTS</div>
<div class="abs hero-tag">Offer the whole world to your clients.</div>
<div class="abs dots"><i class="on"></i><i></i><i></i><i></i></div>

<div class="abs features"></div>
<div class="abs feature" style="left:97px">
  <div class="icon" role="img" aria-label="Silver padlock" style="background:linear-gradient(#e8e8e8,#8d8d8d)"></div>
  <h3>SECURITY</h3><p>Protecting your brand against<br>undersire association</p>
</div>
<div class="abs feature" style="left:351px">
  <div class="icon" role="img" aria-label="Colourful rising bar chart" style="background:linear-gradient(90deg,#8dd3e8,#9fd46b,#f2c14a,#e96a2a)"></div>
  <h3>TLD EXPECILIST</h3><p>Providing a large portfolio for<br>your clients</p>
</div>
<div class="abs feature" style="left:604px">
  <div class="icon" role="img" aria-label="Grey gear with blue centre" style="border-radius:50%;background:radial-gradient(circle,#2f7fd0 25%,#9a9a9a 45%,#666 70%)"></div>
  <h3>AUTOMATION</h3><p>Domain Process:<br>Quick and Reliable</p>
</div>
<div class="abs feature" style="left:858px">
  <div class="icon" role="img" aria-label="Silver alarm clock" style="border-radius:50%;background:radial-gradient(circle,#fff 40%,#b5b5b5 60%,#7a7a7a)"></div>
  <h3>PERSONAL SERVICE</h3><p>High Qualified professionals<br>at your service</p>
</div>

<h2 class="abs welcome-title">WELCOME TO OUR SITE</h2>
<div class="abs welcome-sub">Give your customers a choice of 250 Top Level Domains (TLDs)</div>
<p class="abs welcome-text">Quila is mainly focused the the latin american marked. Today Quila is the fastest growing .br registrar and today many of the world’s largest registrars are using QuilaNIC to register .br domain with or without local present. With the unique QuilaNIC registration engine, you can offer your customers more than 200 top-level domains (TLDs).</p>
<div class="abs btn">View more</div>
<div class="abs photo-frame"><div class="photo" role="img" aria-label="Businessman touching a glowing network of contacts"></div></div>

<div class="abs tab active" style="left:88px">QUILANIC</div>
<div class="abs tab" style="left:295px">QUILADNS</div>
<div class="abs tab" style="left:502px">INFORMAÇÕES DE TLD</div>
<div class="abs tab" style="left:708px">LOCAL PRESENCE</div>
<div class="abs tab" style="left:914px">IDNS</div>

<footer class="abs footer"></footer>
<div class="abs foot-links">Home<span>|</span>Why Quila<span>|</span>Products<span>|</span>Services<span>|</span>Reseller<span>|</span>Contact</div>
<div class="abs copyright">Copyright&nbsp; © 2013&nbsp; www.quilanorte.com&nbsp;&nbsp; All rights reserved.</div>
<div class="abs social">
  <i></i><i></i><i></i>
  <i><svg width="26" height="26" viewBox="0 0 26 26"><rect x="6" y="8" width="14" height="10" fill="none" stroke="#fff" stroke-width="1.5"/><path d="M6 8l7 6 7-6" fill="none" stroke="#fff" stroke-width="1.5"/></svg></i>
</div>

</body>
</html>
```